Velmora - 3D medical animations and high end visual content

Our company creates high end visual content and animations for medical global companies.
Our website - www.velmora-studio.example
We would like to have an amazing business card for our CEO that he can use in the following exhebitions he is going to attend.
It is very important that the design will be memorable and diffrent. It has to reflect our brand design (you can have it from our website)
We would like to transmit innovation, prestige, luxury, aesthetics.
The card has to be Double Sided

Target Market(s)

Marketing managers in medical global companys

Industry/Entity Type

It Company

Contact Information for Business Card

Requirements
Nice to have
• It is very important that the design will be memorable and diffrent. It has to reflect our brand design (you can have it from our website)

```html
<!DOCTYPE html>
<html lang="en">
<head>
<meta charset="utf-8">
<title>Velmora – Business Card</title>
<link href="https://fonts.googleapis.com/css2?family=Open+Sans:wght@400;600;700&display=swap" rel="stylesheet">
<style>
  :root {
    --backdrop: #5a4a3e;
    --card-black: #000000;
    --navy-top: #0b3358;
    --navy-bottom: #020e1c;
    --teal: #1b8ea8;
    --white: #ffffff;
    --grey-text: #b5b5b5;
    --url-grey: #9fb0bd;
    --accent-yellow: #f7c600;
  }
  * { margin: 0; padding: 0; box-sizing: border-box; }
  html, body {
    width: 1200px; height: 987px; overflow: hidden;
    background: var(--backdrop);
    font-family: "Open Sans", Arial, sans-serif;
  }
  .canvas { position: relative; width: 1200px; height: 987px; }
  .card {
    position: absolute; left: 293px; width: 615px; height: 351px;
    border-radius: 19px; overflow: hidden;
    box-shadow: 0 3px 8px rgba(0,0,0,0.35);
  }
  .card-front { top: 130px; background: var(--card-black); }
  .card-back {
    top: 506px;
    background: radial-gradient(ellipse 70% 60% at 62% 0%, var(--navy-top) 0%, #06213d 45%, var(--navy-bottom) 100%);
  }

  .brand-name {
    position: absolute; left: 47px; top: 52px;
    font-size: 40px; font-weight: 600; letter-spacing: 3px;
    color: var(--white); line-height: 1;
  }

  .contact-list { position: absolute; left: 47px; top: 206px; list-style: none; }
  .contact-item {
    display: flex; align-items: center; height: 23.5px;
    font-size: 16px; color: var(--grey-text);
  }
  .contact-icon { width: 16px; height: 16px; margin-right: 10px; fill: var(--teal); }

  .person { position: absolute; right: 37px; top: 223px; text-align: right; }
  .person-name { font-size: 21px; font-weight: 600; color: var(--teal); line-height: 1.2; }
  .person-title { font-size: 16px; color: var(--white); line-height: 1.3; }
  .accent-bar {
    position: absolute; right: 0; top: 232px; width: 11px; height: 41px;
    background: var(--accent-yellow);
  }

  .back-mark {
    position: absolute; left: 0; right: 0; top: 140px;
    display: flex; justify-content: center; align-items: center; gap: 14px;
  }
  .back-dot { width: 22px; height: 22px; border-radius: 50%; background: var(--teal); }
  .back-name {
    font-size: 44px; font-weight: 600; letter-spacing: 4px;
    color: var(--white); line-height: 1;
  }
  .back-url {
    position: absolute; left: 0; right: 0; top: 284px; text-align: center;
    font-size: 15px; letter-spacing: 2.6px; color: var(--url-grey);
  }
</style>
</head>
<body>
<div class="canvas">

  <section class="card card-front" aria-label="Card front">
    <div class="brand-name">VELMORA</div>

    <ul class="contact-list">
      <li class="contact-item">
        <svg class="contact-icon" viewBox="0 0 16 16" aria-hidden="true"><path d="M3.2 1.5l2.4 0 1.2 3.2-1.6 1.1c.8 1.7 2.2 3.1 3.9 3.9l1.1-1.6 3.2 1.2 0 2.4c0 .8-.7 1.5-1.5 1.4C6.6 12.7 3.3 9.4 2.9 3c-.1-.8.5-1.5 1.3-1.5z"/></svg>
        +1-555-014-2077
      </li>
      <li class="contact-item">
        <svg class="contact-icon" viewBox="0 0 16 16" aria-hidden="true"><path d="M4.5 0.5h7c.8 0 1.5.7 1.5 1.5v12c0 .8-.7 1.5-1.5 1.5h-7c-.8 0-1.5-.7-1.5-1.5V2c0-.8.7-1.5 1.5-1.5zM5 2.5v9.5h6V2.5zM8 12.8a.9.9 0 1 0 0 1.8.9.9 0 0 0 0-1.8z"/></svg>
        +1-555-018-7912
      </li>
      <li class="contact-item">
        <svg class="contact-icon" viewBox="0 0 16 16" aria-hidden="true"><path d="M1 3.5h14v9H1zM2.2 4.5L8 9l5.8-4.5z" fill-rule="evenodd"/></svg>
        noam@velmora-studio.example
      </li>
      <li class="contact-item">
        <svg class="contact-icon" viewBox="0 0 16 16" aria-hidden="true"><circle cx="8" cy="8" r="7"/></svg>
        velmora-studio.example
      </li>
    </ul>

    <div class="person">
      <div class="person-name">NOAM CARVER</div>
      <div class="person-title">Founder&amp;CEO</div>
    </div>
    <div class="accent-bar"></div>
  </section>

  <section class="card card-back" aria-label="Card back">
    <div class="back-mark">
      <span class="back-dot"></span>
      <span class="back-name">VELMORA</span>
    </div>
    <div class="back-url">www.velmora-studio.example</div>
  </section>

</div>
</body>
</html>
```